Voltara Solutions Ltd - Project for new electric vehicle charging company

Please use Voltara Solutions Ltd logo & artwork instead of Brightwell.

We would like to produce a leaflet to advertise our electric vehicle charging company to build a reputation and workflow in the local area.

We would like to use the attached logo and maintain the colour palette of the of the logo to be simple, modern and effective.

I have over 15 years experience in the electrical industry and have direct access to the latest technology in electric vehicle charging.

All quotes to remain fixed costs subject to survey of the property and maintenance options can be available.

We can also offer further remedial works to any property through our sister company Brightwell Solutions Ltd.

Target Market(s)

Domestic / commercial customers

Requirements
Must have
• Voltara Solutions Ltd logo and colour palette.
Should not have
• Brightwell logo, Email or website address.

```html
<!DOCTYPE html>
<html lang="en">
<head>
<meta charset="utf-8">
<title>Voltara Solutions Ltd – EV Charging Leaflet</title>
<link href="https://fonts.googleapis.com/css2?family=Poppins:wght@400;500;600;700;800&display=swap" rel="stylesheet">
<style>
  :root {
    --teal: #14b8a0;
    --teal-deep: #0fa58f;
    --ink: #111111;
    --charcoal: #2f3132;
    --white: #ffffff;
    --page: #ededed;
  }
  * { box-sizing: border-box; margin: 0; padding: 0; }
  html, body { width: 1200px; height: 2354px; overflow: hidden; background: var(--page); }
  body { font-family: "Poppins", sans-serif; position: relative; }

  .leaflet {
    position: absolute; left: 100px; top: 472px;
    width: 1000px; height: 1410px; overflow: hidden;
    background: var(--white);
    box-shadow: 0 20px 40px rgba(0,0,0,.25);
  }
  .leaflet > * { position: absolute; }

  .hero-backdrop {
    left: 0; top: 0; width: 1000px; height: 700px;
    background: linear-gradient(180deg, #3a3c3d 0%, #2b2d2e 55%, #333536 100%);
  }
  .shapes { left: 0; top: 0; width: 1000px; height: 1410px; }

  .brand { top: 58px; left: 0; width: 1000px; display: flex; justify-content: center; align-items: center; gap: 18px; }
  .brand-dot { width: 82px; height: 82px; border-radius: 50%; background: var(--teal); }
  .brand-name { color: var(--teal); font-weight: 500; font-size: 58px; line-height: 1; letter-spacing: 1px; }
  .brand-name small { display: block; font-size: 15px; letter-spacing: 9px; margin-top: 6px; }

  .headline { top: 190px; left: 0; width: 1000px; text-align: center; font-weight: 800; font-size: 66px; line-height: 1.0; }
  .headline .line-teal { color: var(--teal); display: block; }
  .headline .line-white { color: var(--white); display: block; margin-top: 6px; }
  .headline-rule { top: 337px; left: 380px; width: 242px; height: 3px; background: var(--teal); }
  .tagline { top: 350px; left: 0; width: 1000px; text-align: center; color: var(--white); font-weight: 600; font-size: 30px; }

  .photo { border-radius: 4px; }
  .photo-car-blue { left: 232px; top: 420px; width: 590px; height: 215px; border-radius: 120px 160px 40px 40px; background: linear-gradient(180deg,#8a9bb8,#6a7b98); }
  .photo-charger-top { left: 888px; top: 378px; width: 48px; height: 240px; border-radius: 20px 20px 6px 6px; background: linear-gradient(90deg,#c9ccd0,#8e9297); }
  .photo-charger-main { left: 498px; top: 835px; width: 116px; height: 345px; border-radius: 50px 50px 10px 10px; background: linear-gradient(90deg,#d9dcdf,#a3a8ad,#e6e8ea); }
  .photo-car-yellow { left: 648px; top: 930px; width: 272px; height: 240px; border-radius: 60px 60px 30px 30px; background: linear-gradient(180deg,#f7b21c,#f09a0c); }

  .revolution { top: 722px; left: 57px; font-weight: 800; font-size: 50px; line-height: 1.05; color: var(--ink); }
  .revolution span { color: var(--teal); }

  .point { left: 62px; display: flex; gap: 24px; align-items: flex-start; }
  .point-1 { top: 862px; }
  .point-2 { top: 1028px; }
  .point-num {
    width: 60px; height: 60px; border-radius: 50%; flex: none;
    background: var(--ink); color: var(--white); border: 3px solid var(--teal);
    display: flex; align-items: center; justify-content: center;
    font-weight: 700; font-size: 34px; margin-top: 2px;
  }
  .point-text { font-size: 20px; line-height: 1.2; color: var(--ink); width: 270px; }
  .point-divider { top: 1008px; left: 75px; width: 395px; height: 2px; background: linear-gradient(90deg,transparent,#777 20%,#777 80%,transparent); }

  .badge {
    left: 628px; top: 650px; width: 304px; height: 304px; border-radius: 50%;
    background: var(--teal); border: 5px solid var(--ink); overflow: hidden; text-align: center; color: var(--white);
  }
  .badge-over { margin-top: 42px; font-size: 27px; font-weight: 600; }
  .badge-band { margin-top: 4px; background: var(--ink); height: 74px; display: flex; align-items: center; justify-content: center; gap: 6px; }
  .badge-num { font-size: 66px; font-weight: 700; letter-spacing: -3px; line-height: 1; }
  .badge-label { font-size: 30px; font-weight: 700; line-height: .95; text-align: left; }
  .badge-copy { margin: 10px auto 0; width: 240px; font-size: 16px; line-height: 1.2; color: var(--ink); }

  .contacts { top: 1262px; left: 60px; width: 900px; display: grid; grid-template-columns: 460px 440px; row-gap: 6px; color: var(--ink); font-weight: 600; font-size: 26px; }
  .contact { display: flex; align-items: center; gap: 12px; }
  .contact svg { width: 24px; height: 24px; flex: none; }
</style>
</head>
<body>
<main class="leaflet">
  <div class="hero-backdrop" role="img" aria-label="Dim photo of cars parked at a charging station"></div>

  <svg class="shapes" viewBox="0 0 1000 1410" aria-hidden="true">
    <path d="M0 480 C120 440 240 470 420 520 C620 570 820 540 1000 520 L1000 720 L0 720 Z" fill="var(--teal)"/>
    <path d="M0 610 C150 690 330 690 520 650 C720 608 860 580 1000 590 L1000 760 L0 760 Z" fill="var(--white)"/>
    <path d="M0 1168 C220 1230 420 1220 620 1190 C800 1162 900 1170 1000 1178 L1000 1200 C880 1188 780 1190 620 1212 C420 1240 220 1252 0 1200 Z" fill="var(--ink)"/>
    <path d="M0 1200 C220 1252 420 1240 620 1212 C780 1190 880 1188 1000 1200 L1000 1410 L0 1410 Z" fill="var(--teal)"/>
  </svg>

  <div class="brand">
    <span class="brand-dot"></span>
    <span class="brand-name">Voltara<small>SOLUTIONS LTD</small></span>
  </div>

  <h1 class="headline"><span class="line-teal">FUELING THE FUTURE</span><span class="line-white">ONE CHARGE AT A TIME</span></h1>
  <div class="headline-rule"></div>
  <p class="tagline">Revolutionizing the Way We Charge Our Vehicles</p>

  <div class="photo photo-car-blue" role="img" aria-label="Blue electric car side view, plugged in"></div>
  <div class="photo photo-charger-top" role="img" aria-label="Wall-standing EV charging post"></div>

  <h2 class="revolution">BE A PART OF<br>OUR <span>REVOLUTION</span></h2>

  <div class="point point-1">
    <span class="point-num">1</span>
    <p class="point-text">All quotes to remain fixed costs subject to survey of the property and maintenance options can be available.</p>
  </div>
  <div class="point-divider"></div>
  <div class="point point-2">
    <span class="point-num">2</span>
    <p class="point-text">We can also offer further remedial works to any property through our sister company Brightwell Solutions Ltd.</p>
  </div>

  <div class="photo photo-charger-main" role="img" aria-label="Silver freestanding EV charger"></div>
  <div class="photo photo-car-yellow" role="img" aria-label="Yellow electric car, rear view"></div>

  <div class="badge">
    <p class="badge-over">OVER</p>
    <div class="badge-band">
      <span class="badge-num">15</span>
      <span class="badge-label">YEARS OF<br>EXPERIENCE</span>
    </div>
    <p class="badge-copy">in the electrical industry and have direct access to the latest technology in electric vehicle charging</p>
  </div>

  <div class="contacts">
    <span class="contact">
      <svg viewBox="0 0 24 24"><path d="M6.6 10.8a15 15 0 0 0 6.6 6.6l2.2-2.2a1 1 0 0 1 1-.25 11.4 11.4 0 0 0 3.6.57 1 1 0 0 1 1 1V20a1 1 0 0 1-1 1A17 17 0 0 1 3 4a1 1 0 0 1 1-1h3.5a1 1 0 0 1 1 1c0 1.25.2 2.45.57 3.57a1 1 0 0 1-.25 1z" fill="var(--ink)"/></svg>
      0200 4150 6262
    </span>
    <span class="contact">
      <svg viewBox="0 0 24 24"><circle cx="12" cy="12" r="9.5" fill="none" stroke="var(--ink)" stroke-width="2"/><ellipse cx="12" cy="12" rx="4" ry="9.5" fill="none" stroke="var(--ink)" stroke-width="2"/><path d="M2.5 12h19" stroke="var(--ink)" stroke-width="2"/></svg>
      www.voltarasolutions.com
    </span>
    <span class="contact">
      <svg viewBox="0 0 24 24"><path d="M2 5h20v14H2z" fill="var(--ink)"/><path d="M2 5l10 8 10-8" fill="none" stroke="var(--teal)" stroke-width="1.6"/></svg>
      info@voltarasolutions.com
    </span>
    <span class="contact">
      <svg viewBox="0 0 24 24"><path d="M12 2a7 7 0 0 0-7 7c0 5 7 13 7 13s7-8 7-13a7 7 0 0 0-7-7z" fill="none" stroke="var(--ink)" stroke-width="2.2"/><circle cx="12" cy="9" r="2.6" fill="var(--ink)"/></svg>
      12 Faraday Court Coventry
    </span>
  </div>
</main>
</body>
</html>
```